Directing people to check over 2000 new Portugal listings on the site

A copy of our failed attempt is annexed. graphics should be 197x650px and 448x81px

Target Market(s)

Global property Buyers

Requirements
Nice to have
• Euro map with portugal isolated

```html
<!DOCTYPE html>
<html lang="en">
<head>
<meta charset="utf-8">
<title>2000 New Listings in the Mediterranean – Banners</title>
<link rel="stylesheet" href="https://fonts.googleapis.com/css2?family=Roboto+Condensed:wght@700&family=PT+Sans:wght@700&display=swap">
<style>
  :root {
    --stage: #3a2617;
    --blue-deep: #153f8c;
    --blue-mid: #1c63b8;
    --blue-light: #2a8ed6;
    --yellow: #ffe81a;
    --white: #ffffff;
    --red: #c8232c;
    --navy-text: #233a8f;
    --dark-text: #2a2a2a;
    --map-sea: #8fd0ea;
    --map-land: #9bd38f;
    --map-sand: #f3d9a6;
    --label: #f2f2f2;
  }
  * { box-sizing: border-box; margin: 0; padding: 0; }
  html, body { width: 1200px; height: 1200px; overflow: hidden; }
  body { background: var(--stage); position: relative; font-family: "Roboto Condensed", "Arial Narrow", sans-serif; }

  .size-label {
    position: absolute; color: var(--label);
    font-family: "PT Sans", Arial, sans-serif; font-weight: 400; font-size: 30px;
  }
  .size-label--sky { left: 162px; top: 36px; }
  .size-label--leader { left: 995px; top: 470px; }

  .banner { position: absolute; overflow: hidden; background: var(--white); box-shadow: 4px 6px 14px rgba(0,0,0,.55); }
  .banner svg.shapes { position: absolute; inset: 0; }

  /* Skyscraper 197x650 */
  .skyscraper { left: 94px; top: 118px; width: 297px; height: 982px; }
  .skyscraper .map-area {
    position: absolute; left: 0; top: 270px; width: 297px; height: 640px;
    background: linear-gradient(180deg, var(--map-land) 0%, var(--map-sea) 30%, var(--map-land) 50%, var(--map-sand) 72%, var(--white) 92%);
  }
  .skyscraper .headline {
    position: absolute; left: 0; top: 40px; width: 100%; text-align: center;
    color: var(--yellow); font-size: 56px; line-height: 60px; font-weight: 700;
    text-shadow: 2px 3px 4px rgba(0,0,0,.45);
  }
  .skyscraper .subhead {
    position: absolute; left: 0; top: 172px; width: 100%; text-align: center;
    color: var(--white); font-size: 36px; line-height: 42px; font-weight: 700;
    text-shadow: 2px 2px 3px rgba(0,0,0,.4);
  }
  .skyscraper .cta-text {
    position: absolute; left: 0; top: 810px; width: 100%; text-align: center;
    color: var(--navy-text); font-family: "PT Sans", Arial, sans-serif;
    font-size: 28px; line-height: 35px; font-weight: 700;
  }
  .skyscraper .click-arrow { position: absolute; left: 182px; top: 296px; width: 104px; height: 80px; }

  /* Leaderboard 448x81 */
  .leaderboard { left: 461px; top: 550px; width: 678px; height: 122px; }
  .leaderboard .map-area {
    position: absolute; left: 0; top: 0; width: 130px; height: 122px;
    background: linear-gradient(90deg, var(--map-sand) 0%, var(--map-land) 35%, var(--map-sea) 65%, var(--white) 100%);
  }
  .leaderboard .cta-text {
    position: absolute; left: 118px; top: 14px; width: 150px;
    color: var(--dark-text); font-family: "PT Sans", Arial, sans-serif;
    font-size: 16px; line-height: 22px; font-weight: 700;
  }
  .leaderboard .headline {
    position: absolute; left: 268px; top: 12px; width: 400px; text-align: center;
    color: var(--white); font-size: 42px; line-height: 46px; font-weight: 700;
    text-shadow: 2px 2px 3px rgba(0,0,0,.4);
  }
  .leaderboard .subhead {
    position: absolute; left: 268px; top: 64px; width: 410px; text-align: center;
    color: var(--white); font-size: 30px; line-height: 34px; font-weight: 700;
    text-shadow: 1px 2px 3px rgba(0,0,0,.4);
  }
  .leaderboard .click-arrow { position: absolute; left: 228px; top: 72px; width: 76px; height: 46px; }
</style>
</head>
<body>
  <div class="size-label size-label--sky">197x650</div>
  <div class="size-label size-label--leader">448x81</div>

  <section class="banner skyscraper">
    <div class="map-area" role="img" aria-label="Map of Europe and North Africa with Portugal circled in red"></div>
    <svg class="shapes" viewBox="0 0 297 982" preserveAspectRatio="none" aria-hidden="true">
      <defs>
        <linearGradient id="skyBlue" x1="0" y1="0" x2="0" y2="1">
          <stop offset="0" stop-color="var(--blue-light)"/>
          <stop offset="0.6" stop-color="var(--blue-mid)"/>
          <stop offset="1" stop-color="var(--blue-deep)"/>
        </linearGradient>
      </defs>
      <path d="M0 0 H297 V395 C230 395 150 360 80 320 C50 304 25 295 0 290 Z" fill="url(#skyBlue)"/>
      <path d="M0 290 C25 295 50 304 80 320 C150 360 230 395 297 395 V410 C225 410 145 378 78 340 C48 322 25 312 0 306 Z" fill="var(--red)"/>
      <path d="M0 306 C25 312 48 322 78 340 C145 378 225 410 297 410 V422 C220 422 140 392 74 356 C46 340 22 330 0 326 Z" fill="var(--white)"/>
    </svg>
    <h1 class="headline">2000 NEW<br>LISTINGS</h1>
    <p class="subhead">IN THE<br>MEDITERRANEAN</p>
    <svg class="click-arrow" viewBox="0 0 104 80" aria-hidden="true">
      <g transform="rotate(-35 52 40)">
        <polygon points="6,40 30,18 30,28 96,28 96,52 30,52 30,62" fill="var(--white)" stroke="#9aa" stroke-width="1"/>
        <text x="64" y="45" text-anchor="middle" font-family="PT Sans, Arial, sans-serif" font-weight="700" font-size="14" fill="var(--dark-text)">Click now</text>
      </g>
    </svg>
    <p class="cta-text">Check over 2000<br>new Portugal<br>listings<br>on the site</p>
  </section>

  <section class="banner leaderboard">
    <div class="map-area" role="img" aria-label="Small map of Europe with Portugal circled in red"></div>
    <svg class="shapes" viewBox="0 0 678 122" preserveAspectRatio="none" aria-hidden="true">
      <defs>
        <linearGradient id="leaderBlue" x1="0" y1="0" x2="1" y2="0">
          <stop offset="0" stop-color="var(--blue-light)"/>
          <stop offset="0.5" stop-color="var(--blue-mid)"/>
          <stop offset="1" stop-color="var(--blue-deep)"/>
        </linearGradient>
      </defs>
      <path d="M284 0 C270 40 262 80 252 122 H678 V0 Z" fill="url(#leaderBlue)"/>
      <path d="M276 0 C262 40 252 80 242 122 H252 C262 80 270 40 284 0 Z" fill="var(--red)"/>
    </svg>
    <p class="cta-text">Check Over 2000<br>New Portugal<br>Listings On<br>The Site</p>
    <svg class="click-arrow" viewBox="0 0 76 46" aria-hidden="true">
      <g transform="rotate(-20 38 23)">
        <polygon points="3,23 20,9 20,15 72,15 72,31 20,31 20,37" fill="var(--white)" stroke="#9aa" stroke-width="1"/>
        <text x="46" y="27" text-anchor="middle" font-family="PT Sans, Arial, sans-serif" font-weight="700" font-size="10" fill="var(--dark-text)">Click now</text>
      </g>
    </svg>
    <h2 class="headline">2000 NEW LISTINGS</h2>
    <p class="subhead">IN THE MEDITERRANEAN</p>
  </section>
</body>
</html>
```